Business Card Design

We need a business card designed for a new company based in Melbourne called KPo solutions. KPo solutions provides management consulting specialising in the health and social services sector.

KPo solutions offer a unique set of specialist skills │dealing with all levels of government │ unique communication skills│intimate knowledge of the health sector │solutions tailored to unique circumstances.

KPo solutions takes on a select number of clients at any one time, this ensures that your organisation receives the attention required. On larger projects, KPo solutions join up with other consultants to bring specialist skills to a project.
Updates

This is the first time I have used Pattern Hive and thank you all for responding. The variation is amazing and makes it hard to decide. I have to ask some of my friends to give me their views. The response is fantastic. The one I pick will basically be the most visually appealing

Industry/Entity Type

Management Consulting

Contact Information for Business Card

Martin Hollis, Principal, KPo solutions, 14 Calloway Ave, Westbridge VIC 3094, 0438 712 304, martinh@kposolutions.com.au, www.kposolutions.com.au

```html
<!DOCTYPE html>
<html lang="en">
<head>
<meta charset="utf-8">
<title>KPo solutions – Business Card</title>
<link rel="stylesheet" href="https://fonts.googleapis.com/css2?family=Open+Sans:wght@400;600&family=Graduate&display=swap">
<style>
  :root {
    --page-bg: #f2f2f2;
    --brand-red: #b8202c;
    --brand-red-light: #c73a44;
    --card-black: #141414;
    --card-black-soft: #2a2a2a;
    --silver-dark: #8a8a8a;
    --silver-light: #f4f4f4;
    --logo-grey: #dcdcdc;
    --tagline-ink: #161616;
    --name-red: #c8262f;
    --text-white: #f5f5f5;
  }
  * { box-sizing: border-box; margin: 0; padding: 0; }
  html, body {
    width: 1200px; height: 900px; overflow: hidden;
    background: var(--page-bg);
  }
  .business-card {
    position: absolute;
    left: 150px; top: 170px;
    width: 900px; height: 560px;
    border-radius: 36px;
    overflow: hidden;
    box-shadow: 0 18px 40px rgba(0,0,0,0.18);
    font-family: "Open Sans", "Segoe UI", sans-serif;
  }
  .brand-band {
    position: absolute; left: 0; top: 0;
    width: 100%; height: 290px;
    background: var(--brand-red);
  }
  .brand-texture {
    position: absolute; right: 0; top: 0;
    width: 230px; height: 290px;
    background: linear-gradient(135deg, var(--brand-red-light), var(--brand-red));
  }
  .brand-lockup {
    position: absolute; left: 64px; top: 86px;
    display: inline-flex; flex-direction: column; align-items: flex-end;
    gap: 22px;
  }
  .brand-name {
    font-size: 66px; font-weight: 600;
    line-height: 1;
    letter-spacing: 2px;
    text-transform: uppercase;
    color: var(--logo-grey);
  }
  .brand-tagline {
    font-family: "Graduate", "Rockwell", serif;
    font-size: 20px; letter-spacing: 0.5px;
    color: var(--tagline-ink);
  }
  .silver-rule {
    position: absolute; left: 0; top: 290px;
    width: 100%; height: 12px;
    background: linear-gradient(180deg, var(--silver-dark), var(--silver-light) 50%, var(--silver-dark));
  }
  .contact-panel {
    position: absolute; left: 0; top: 302px;
    width: 100%; height: 258px;
    background: linear-gradient(180deg, var(--card-black-soft), var(--card-black));
    padding: 20px 0 0 70px;
  }
  .person-name {
    font-size: 29px; font-weight: 600;
    color: var(--name-red); line-height: 1.2;
  }
  .person-role {
    font-size: 22px; color: var(--text-white);
    line-height: 1.3; margin-bottom: 24px;
  }
  .contact-list { list-style: none; }
  .contact-item {
    display: flex; align-items: center; gap: 14px;
    font-size: 22px; color: var(--text-white);
    line-height: 30px;
  }
  .contact-icon { width: 24px; height: 24px; flex: none; fill: var(--name-red); }
</style>
</head>
<body>
  <article class="business-card">
    <header class="brand-band">
      <div class="brand-texture" role="img" aria-label="Subtle repeating cross pattern in tonal red"></div>
      <div class="brand-lockup">
        <div class="brand-name">KPo solutions</div>
        <div class="brand-tagline">HEALTH &amp; SOCIAL SERVICES CONSULTING</div>
      </div>
    </header>
    <div class="silver-rule"></div>
    <section class="contact-panel">
      <h1 class="person-name">Martin Hollis</h1>
      <p class="person-role">Principal</p>
      <ul class="contact-list">
        <li class="contact-item">
          <svg class="contact-icon" viewBox="0 0 24 24" aria-hidden="true"><path d="M6.6 10.8a15.1 15.1 0 0 0 6.6 6.6l2.2-2.2a1 1 0 0 1 1-.25 11.4 11.4 0 0 0 3.6.6 1 1 0 0 1 1 1V20a1 1 0 0 1-1 1A17 17 0 0 1 3 4a1 1 0 0 1 1-1h3.5a1 1 0 0 1 1 1c0 1.25.2 2.45.6 3.6a1 1 0 0 1-.25 1z"/></svg>
          0438 712 304,
        </li>
        <li class="contact-item">
          <svg class="contact-icon" viewBox="0 0 24 24" aria-hidden="true"><path d="M2 6h20v13H2z M3 7l9 7 9-7" stroke="#141414" stroke-width="1.4"/></svg>
          martinh@kposolutions.com.au
        </li>
        <li class="contact-item">
          <svg class="contact-icon" viewBox="0 0 24 24" aria-hidden="true"><circle cx="12" cy="12" r="10"/><path d="M2 12h20M12 2c3 3 3 17 0 20M12 2c-3 3-3 17 0 20M4 7h16M4 17h16" stroke="#141414" stroke-width="1.3" fill="none"/></svg>
          www.kposolutions.com.au
        </li>
        <li class="contact-item">
          <svg class="contact-icon" viewBox="0 0 24 24" aria-hidden="true"><path d="M12 3 1.5 12H5v9h5.5v-6h3v6H19v-9h3.5z"/></svg>
          14 Calloway Ave, Westbridge VIC 3094
        </li>
      </ul>
    </section>
  </article>
</body>
</html>
```